Veloma Realty Business Cards template for all our agents.

Create a template for Business Cards for our agents. We would need to have access to the source file in order to change info for each agent. We want color and not all white cards. We would like to see movements and texture in the design. Use the colors in the file included plus neutral colors back, white and grey. we would like to see some designs with the logo on the front and some on the back.

Target Market(s)

Real Estate

Industry/Entity Type

Real Estate

Contact Information for Business Card

Please create a template for our business cards. Dimensions 3.5 x 2

We would like
• Spot for an agent photo. (On front of card)
• Logo
• Position (mainly Homeguild ®)
• Mobile
• Fax.
• Email
• Website
• Equal housing logo
• Homeguild logo
• Text – “Search property listings like an agent!”
• Our address 4527 Fennick Row, Suite 3, Dalemont, OR 97458
• Our colors are attached.
• Not boxy
• DO NOT HAVE AGENT PHOTO CUT OUT.

Requirements
Must have
• • Spot for an agent photo. (On front of card)
• • Logo
• • Position (mainly Homeguild ®)
• • Mobile
• • Fax.
• • Email
• • Website
• • Equal housing logo
• • Homeguild logo
• • Text – “Search property listings like an agent!”
• • Our address 4527 Fennick Row, Suite 3, Dalemont, OR 97458
Should not have
• BOXY

```html
<!DOCTYPE html>
<html lang="en">
<head>
<meta charset="utf-8">
<title>Veloma Realty Group – Agent Business Card</title>
<link href="https://fonts.googleapis.com/css2?family=Montserrat:wght@300;400;600;700&display=swap" rel="stylesheet">
<style>
  :root {
    --page-bg: #2a2a2a;
    --card-black: #0d0d0d;
    --card-black-2: #1c1c1c;
    --plum: #6e2a4e;
    --leaf: #6f8f3c;
    --white: #ffffff;
    --grey: #9a9a9a;
    --grey-dark: #5a5a5a;
  }
  html, body {
    margin: 0;
    width: 1200px;
    height: 900px;
    overflow: hidden;
    background: var(--page-bg);
    font-family: "Montserrat", sans-serif;
  }
  .sheet {
    position: relative;
    width: 1200px;
    height: 900px;
  }
  .card {
    position: absolute;
    left: 250px;
    width: 700px;
    height: 400px;
    overflow: hidden;
    background: linear-gradient(135deg, var(--card-black-2) 0%, var(--card-black) 55%, #050505 100%);
    box-shadow: 0 10px 30px rgba(0,0,0,.45);
  }
  .card--back { top: 30px; }
  .card--front { top: 470px; }

  /* back */
  .brand {
    position: absolute;
    display: flex;
    align-items: center;
    gap: 14px;
  }
  .brand__dot {
    width: 46px;
    height: 46px;
    border-radius: 50%;
    background: var(--grey-dark);
  }
  .brand__name {
    font-weight: 600;
    line-height: 1.05;
    letter-spacing: 2px;
    text-transform: uppercase;
  }
  .brand__name small { display: block; font-size: .48em; letter-spacing: 3px; }
  .card--back .brand { left: 50%; top: 130px; transform: translateX(-50%); }
  .card--back .brand__name { font-size: 40px; color: var(--grey); }
  .tagline {
    position: absolute;
    left: 0; right: 0;
    top: 262px;
    margin: 0;
    text-align: center;
    color: var(--white);
    font-size: 17px;
    font-weight: 400;
    letter-spacing: .5px;
    text-transform: uppercase;
  }

  /* front */
  .card--front .brand { right: 30px; top: 26px; gap: 10px; }
  .card--front .brand__dot { width: 34px; height: 34px; background: var(--plum); }
  .card--front .brand__name { font-size: 28px; color: var(--leaf); }
  .portrait { position: absolute; inset: 0; }
  .agent {
    position: absolute;
    left: 30px;
    top: 336px;
    color: var(--white);
  }
  .agent__name { font-size: 22px; font-weight: 300; letter-spacing: .5px; margin: 0; }
  .agent__name b { font-weight: 700; }
  .agent__title { font-size: 15px; color: #cfcfcf; margin: 0; }
  .contact {
    position: absolute;
    right: 30px;
    top: 150px;
    list-style: none;
    margin: 0;
    padding: 0;
    text-align: right;
    color: var(--white);
    font-size: 15px;
    line-height: 30px;
  }
  .contact li { display: flex; justify-content: flex-end; align-items: center; gap: 10px; }
  .contact svg { width: 14px; height: 14px; fill: var(--plum); }
  .contact .address { display: block; line-height: 22px; margin-top: 6px; padding-right: 24px; }
</style>
</head>
<body>
<main class="sheet">

  <section class="card card--back" aria-label="Card back">
    <div class="brand">
      <span class="brand__dot"></span>
      <span class="brand__name">Veloma<small>Realty Group</small></span>
    </div>
    <p class="tagline">Search property listings like an agent</p>
  </section>

  <section class="card card--front" aria-label="Card front">
    <svg class="portrait" width="700" height="400" viewBox="0 0 700 400">
      <defs>
        <linearGradient id="photoTone" x1="0" y1="0" x2="1" y2="1">
          <stop offset="0" stop-color="#dfe4ea"/>
          <stop offset=".55" stop-color="#b99a82"/>
          <stop offset="1" stop-color="#6b4e3c"/>
        </linearGradient>
      </defs>
      <path d="M330,110 H352 C478,140 535,290 446,400 H420 C505,280 445,140 330,110 Z" fill="var(--plum)"/>
      <path role="img" aria-label="Agent portrait photo" d="M0,110 H330 C445,140 505,280 420,400 H0 Z" fill="url(#photoTone)"/>
      <path d="M0,325 H330 L305,400 H0 Z" fill="rgba(10,10,10,.85)"/>
      <rect x="322" y="310" width="30" height="30" fill="none" stroke="#fff" stroke-width="3"/>
      <rect x="362" y="310" width="30" height="30" fill="#fff"/>
    </svg>
    <div class="agent">
      <p class="agent__name"><b>YOUR</b> NAME</p>
      <p class="agent__title">Job Title</p>
    </div>

    <div class="brand">
      <span class="brand__dot"></span>
      <span class="brand__name">Veloma<small>Realty Group</small></span>
    </div>

    <ul class="contact">
      <li>000 000 0000
        <svg viewBox="0 0 14 14"><path d="M3 1l3 3-2 2c1 2 2 3 4 4l2-2 3 3-2 2C6 13 1 8 1 3z"/></svg></li>
      <li>000 000 0000
        <svg viewBox="0 0 14 14"><rect x="3" y="1" width="8" height="4"/><rect x="1" y="5" width="12" height="6" rx="1"/><rect x="3" y="9" width="8" height="4"/></svg></li>
      <li>youremail@xyz.com
        <svg viewBox="0 0 14 14"><path d="M1 3h12v8H1z M1 3l6 5 6-5" stroke="#0d0d0d" stroke-width="1"/></svg></li>
      <li>www.yourwebsite.com
        <svg viewBox="0 0 14 14"><circle cx="7" cy="7" r="6"/><path d="M1 7h12M7 1v12" stroke="#0d0d0d" stroke-width="1"/></svg></li>
      <li class="address">4527 Fennick Row, Suite 3<br>Dalemont, OR 97458</li>
    </ul>
  </section>

</main>
</body>
</html>
```